Trelvane Summit Flyer to describe services

I provide data abstraction and consulting services to hospitals that are participating in an accreditation program for their bariatric surgery program. I need a flyer that I can hand out to potential clients that describes the services that I offer. I am attaching an info sheet that has the information on the services I offer. (One exception is that I no longer offer the remote dietitian services listed on the flyer) . I am also including a file with my logo. I would like this flyer to hand out at conferences where I meet people that might not be familiar with my business or who are not knowledgeable of how my services might benefit them. The most important service that I offer is the data abstraction subcontracting. I will provide a PPT that will provide further info on this service.

Target Market(s)

Bariatric program directors and surgeons

Industry/Entity Type

Healthcare

Font styles to use
Serif
Sans Serif

Colors

Designer to choose colors to be used in the design.

Requirements
Must have
• a description of the services I offer
• how subcontracting will benefit them and save them money
• something noting my experience as I am one of the most experienced professionals in this field of bariatric surgery accreditation
Nice to have
• I am not a designer and created the flyer that I have provided. I realize it is not very professional and would like something that looks fresh and professional.
Should not have
• I don't want it to be too wordy and yet it needs to have a description of services offered. I want to include the yellow in my logo, but the flyer sample I have given you has waaaaay too much yellow and want to tone that down!

```html
<!DOCTYPE html>
<html lang="en">
<head>
<meta charset="utf-8">
<title>Maren Ashcroft Consulting – Services Flyer</title>
<link href="https://fonts.googleapis.com/css2?family=Montserrat:wght@300;400;600;700;800&family=Lato:wght@400;700&display=swap" rel="stylesheet">
<style>
  :root {
    --yellow: #fdc31b;
    --yellow-pale: #fde38a;
    --ink: #1f1f1f;
    --gray: #555555;
    --paper: #ffffff;
    --dark-veil: rgba(40, 40, 45, 0.78);
  }
  * { box-sizing: border-box; margin: 0; padding: 0; }
  html, body { width: 946px; height: 1200px; overflow: hidden; background: var(--paper); }
  body { font-family: "Lato", sans-serif; color: var(--ink); position: relative; }

  .frame { position: absolute; inset: 11px; border: 1px dashed #8a8a8a; pointer-events: none; z-index: 5; }

  .top-tab { position: absolute; left: 107px; top: 0; width: 142px; height: 74px; background: var(--yellow); }
  .top-rule { position: absolute; left: 0; right: 0; top: 74px; height: 3px; background: var(--yellow); }

  .hero-photo {
    position: absolute; left: 0; right: 0; top: 77px; height: 388px;
    background: linear-gradient(160deg, #eef0f2 0%, #d9dcdf 35%, #8f8a86 60%, #3f4048 85%, #2b2d33 100%);
  }
  .hero-bar { position: absolute; left: 0; right: 0; top: 465px; height: 12px; background: var(--yellow); }

  .brand {
    position: absolute; left: 38px; top: 92px;
    display: flex; align-items: center; gap: 12px;
    font-family: "Montserrat", sans-serif; font-weight: 800; color: var(--ink);
    font-size: 34px; letter-spacing: -0.5px; line-height: 1; white-space: nowrap;
  }
  .brand-square { width: 26px; height: 26px; background: var(--yellow); }

  .tagline {
    position: absolute; left: 44px; top: 218px; width: 423px; height: 55px;
    background: rgba(253, 195, 27, 0.88);
    font-family: "Montserrat", sans-serif; font-weight: 600; font-size: 27px;
    color: var(--ink); padding: 13px 0 0 9px; letter-spacing: 0.3px; white-space: nowrap;
  }
  .program-name {
    position: absolute; left: 44px; top: 289px; width: 334px; height: 59px;
    background: var(--dark-veil);
    font-family: "Montserrat", sans-serif; font-weight: 800; font-size: 48px;
    color: var(--yellow); padding: 2px 0 0 8px; line-height: 56px;
  }

  .feature-title {
    position: absolute; left: 30px; width: 315px; top: 524px; text-align: right;
    font-family: "Montserrat", sans-serif; font-weight: 700; font-size: 29px; line-height: 37px;
  }
  .feature-title .accent { color: var(--yellow); display: block; padding-right: 7px; }
  .feature-title .plain { color: var(--ink); display: block; }
  .feature-divider { position: absolute; left: 369px; top: 514px; width: 2px; height: 136px; background: var(--ink); }
  .feature-text {
    position: absolute; left: 390px; top: 528px; width: 515px;
    font-size: 13.4px; line-height: 15.4px; color: var(--ink);
  }

  .service { position: absolute; top: 690px; width: 192px; }
  .service-head { position: relative; height: 85px; }
  .service-icon { position: absolute; left: 6px; bottom: 20px; width: 32px; height: 32px; }
  .service-stem { position: absolute; left: 42px; bottom: 0; width: 2px; height: 60px; background: var(--yellow); }
  .service-stem::before { content: ""; position: absolute; left: -2px; top: -5px; width: 6px; height: 6px; background: var(--yellow); }
  .service-label {
    position: absolute; left: 54px; bottom: 17px; white-space: nowrap;
    font-family: "Montserrat", sans-serif; font-size: 16px; line-height: 19px; color: var(--gray); font-weight: 400;
  }
  .service-label strong { display: block; color: var(--yellow); font-weight: 700; }
  .service-label.tight { font-size: 15px; line-height: 16px; bottom: 9px; }
  .service-label.tight strong { font-size: 13.5px; line-height: 16px; letter-spacing: -0.4px; }
  .service-body {
    height: 294px; background: var(--yellow-pale);
    padding: 14px 8px 0; text-align: center;
    font-size: 13.2px; line-height: 15.4px; color: var(--ink);
  }

  .portrait {
    position: absolute; left: 745px; top: 1048px; width: 190px; height: 152px;
    border-radius: 95px 95px 0 0;
    background: radial-gradient(circle at 50% 40%, #d8d8d8 0%, #a9a9a9 55%, #7d7d7d 100%);
    z-index: 3;
  }

  .footer { position: absolute; left: 0; right: 0; top: 1116px; height: 84px; background: var(--yellow); }
  .footer-name {
    position: absolute; left: 380px; top: 1131px; white-space: nowrap;
    font-size: 14.5px; font-weight: 700; color: var(--ink); z-index: 4;
  }
  .contact { position: absolute; top: 1158px; display: flex; align-items: center; gap: 12px; font-size: 14px; font-weight: 700; color: var(--ink); z-index: 4; white-space: nowrap; }
  .contact svg { width: 24px; height: 22px; flex: none; }
</style>
</head>
<body>
  <div class="frame"></div>

  <div class="top-tab"></div>
  <div class="top-rule"></div>

  <div class="hero-photo" role="img" aria-label="Photo of a consultant presenting at a whiteboard to seated hospital staff in a bright meeting room"></div>
  <div class="hero-bar"></div>

  <div class="brand"><span>MAREN ASHCROFT CONSULTING</span><span class="brand-square"></span></div>

  <div class="tagline">HELPING YOU NAVIGATE</div>
  <div class="program-name">NBSQAP</div>

  <h1 class="feature-title">
    <span class="accent">DATA</span>
    <span class="accent">ABSTRACTION</span>
    <span class="plain">SUBCONTRACTING</span>
  </h1>
  <div class="feature-divider"></div>
  <p class="feature-text">It is a long established fact that a reader will be distracted by the readable content of a page when looking at its layout. The point of using Lorem Ipsum is that it has a more-or-less normal distribution of letters, as opposed to using 'Content here, content here', making it look like readable English. Many desktop publishing packages and web page editors now use Lorem Ipsum as their default model text, and a search for 'lorem ipsum' will uncover many web sites still in their infancy. Various versions have evolved over the years, sometimes by accident.</p>

  <section class="service" style="left:46px">
    <div class="service-head">
      <svg class="service-icon" viewBox="0 0 32 32" fill="none" stroke="var(--yellow)" stroke-width="2"><path d="M6 3h14l6 6v20H6z"/><path d="M10 12h10M10 17h6M10 22h5"/><circle cx="20" cy="21" r="4"/><path d="M23 24l4 4"/></svg>
      <div class="service-stem"></div>
      <div class="service-label">PROGRAM<strong>ASSESSMENT</strong></div>
    </div>
    <div class="service-body">A 2-day on-site assessment of your bariatric program as it relates to nbsqap compliance, best practice, business strategies and evaluation of the process for collecting outcomes data. a comprehensive post-assessment review and written report will provide guidance, solutions, timelines and suggest opportunities for improvement.</div>
  </section>

  <section class="service" style="left:267px">
    <div class="service-head">
      <svg class="service-icon" viewBox="0 0 32 32" fill="var(--yellow)"><circle cx="9" cy="7" r="4"/><path d="M3 14h12v14H3z"/><path d="M18 14h11v12H18z"/><path d="M20 20l3 3 5-6" stroke="#fff" stroke-width="2" fill="none"/></svg>
      <div class="service-stem"></div>
      <div class="service-label tight">PROGRAM<br>DEVELOPMENT—<strong>REMOTE ASSISTANCE<br>AND ON-SITE</strong></div>
    </div>
    <div class="service-body">For centers currently developing a new program, assistance by experienced professionals can help to ensure accreditation and provide guidance in the development of policies and procedures, job descriptions, clinical pathways and protocols that will enhance program development as well as ensure nbsqap compliance. with the remote option consultant will meet with staff during regularly scheduled webinars.</div>
  </section>

  <section class="service" style="left:488px">
    <div class="service-head">
      <svg class="service-icon" viewBox="0 0 32 32" fill="var(--yellow)"><circle cx="9" cy="9" r="3"/><circle cx="16" cy="7" r="3"/><circle cx="23" cy="9" r="3"/><path d="M2 16h28v4H2zM5 20h22v8H5z"/></svg>
      <div class="service-stem"></div>
      <div class="service-label">NBSCR<strong>STAFFING</strong></div>
    </div>
    <div class="service-body">Maintain compliance with nbsqap data abstraction with a data abstractor who will be a member of your team, provide leadership and direction in the development of qi projects, perform routine quality assurance audits on data and attend all bariatric team meetings.</div>
  </section>

  <section class="service" style="left:709px">
    <div class="service-head">
      <svg class="service-icon" viewBox="0 0 32 32" fill="none" stroke="var(--yellow)" stroke-width="2"><path d="M6 4h16v24H6z"/><path d="M10 10h2M10 16h2M10 22h2M15 10h4M15 16h4"/><circle cx="23" cy="22" r="6" fill="var(--yellow)" stroke="none"/><path d="M20 22l2 2 4-4" stroke="#fff"/></svg>
      <div class="service-stem"></div>
      <div class="service-label">MOCK SITE<strong>INSPECTIONS</strong></div>
    </div>
    <div class="service-body">This one-day rigorous evaluation of a facility evaluates accreditation readiness by providing a critical assessment of all areas related to the standards for nbsqap accreditation. it closely mirrors the nbsqap site survey process.</div>
  </section>

  <div class="footer"></div>
  <div class="portrait" role="img" aria-label="Portrait photo of the consultant, shown in grayscale"></div>
  <div class="footer-name">Maren Ashcroft, RN, CBN Bariatric Program Consultant</div>

  <div class="contact" style="left:44px">
    <svg viewBox="0 0 24 22" fill="none" stroke="#fff" stroke-width="1.6"><rect x="1" y="4" width="22" height="15"/><path d="M1 4l11 9 11-9"/></svg>
    <span>maren@ashcroftconsulting.com</span>
  </div>
  <div class="contact" style="left:351px">
    <svg viewBox="0 0 24 22" fill="#fff"><path d="M6 2l4 5-2 3c1 3 3 5 6 6l3-2 5 4-3 3C10 21 3 13 3 5z"/></svg>
    <span>555-014-2280</span>
  </div>
  <div class="contact" style="left:500px">
    <svg viewBox="0 0 24 22" fill="none" stroke="#fff" stroke-width="1.4"><circle cx="12" cy="11" r="9"/><ellipse cx="12" cy="11" rx="4" ry="9"/><path d="M3 11h18M5 6h14M5 16h14"/></svg>
    <span>ashcroftconsulting.com</span>
  </div>
</body>
</html>
```